Torven Medical needs bold attention catching website for healthcare professionals(target)

I need a hero page as well as a products and about page for a website of mine. I specialize in orthopedic instruments . Specifically bone drills and saws. This whole company was founded to bring superb quality highly discounted medical instruments. Specifically bone drills, bone saws, k-wires and pins. Two main points should be cost savings and superior quality.

Target Market(s)

healthcare professionals Surgeons and hospital material managers

Number of Pages Required

3 page

Font styles to use
Serif

Colors

Designer to choose colors to be used in the design.

Requirements
Must have
• colors should match logo design

```html
<!DOCTYPE html>
<html lang="en">
<head>
<meta charset="utf-8">
<title>Torven Medical</title>
<link href="https://fonts.googleapis.com/css2?family=Open+Sans:wght@400;600;700&display=swap" rel="stylesheet">
<style>
:root{
  --accent:#a0471a;
  --accent-dark:#7a3410;
  --teal:#1b9aa5;
  --lime:#adff2f;
  --ink:#222;
  --muted:#444;
  --line:#e2e2e2;
  --band:#f5f7f9;
  --footer:#2f3640;
}
*{box-sizing:border-box;margin:0;padding:0}
html,body{width:1200px;height:5340px;overflow:hidden}
body{font-family:"Open Sans",Arial,sans-serif;color:var(--ink);background:#fff;position:relative}
.abs{position:absolute}
a{color:inherit;text-decoration:none}

.site-header{top:0;left:0;width:1200px;height:145px}
.brand{left:30px;top:48px;display:flex;align-items:center;gap:10px;font-size:34px;font-weight:600;color:var(--accent)}
.brand-dot{width:16px;height:16px;border-radius:50%;background:var(--accent)}
.main-nav{right:20px;top:58px;display:flex;gap:20px;font-size:15px;color:#333}
.main-nav a:first-child{color:var(--accent)}

.hero{top:145px;left:12px;width:1176px;height:553px;background:linear-gradient(135deg,#3fb3b0,#2a9c9c 45%,#5ec3c0);overflow:hidden}
.hero-copy{left:175px;top:175px;color:#fff;width:820px}
.hero-kicker{font-size:19px;font-weight:600}
.hero-title{font-size:38px;font-weight:700;margin-top:8px}
.hero-title span{color:var(--accent)}
.hero-text{font-size:14px;line-height:1.6;margin-top:6px;width:820px}
.btn-brown{display:inline-block;background:var(--accent);color:#fff;font-size:14px;padding:6px 14px;border-radius:3px;margin-top:16px}
.hero-arrow{top:260px;color:#fff;font-size:30px;opacity:.8}
.hero-dots{left:570px;bottom:20px;display:flex;gap:6px}
.hero-dots i{width:8px;height:8px;background:var(--accent);display:block}
.hero-dots i+i{background:#fff}

.about-img{top:786px;left:16px;width:470px;height:270px;background:linear-gradient(135deg,#6f8a93,#2e4a52 60%,#4a6a72)}
.about-copy{top:786px;left:518px;width:672px}
.eyebrow{font-size:23px;color:#333}
.section-h{font-size:42px;font-weight:400;line-height:1.25;color:#222}
.section-h span{color:var(--accent)}
.body-text{font-size:14.5px;line-height:1.75;color:var(--muted)}

.activity-copy{top:1208px;left:16px;width:670px}
.video{top:1208px;left:718px;width:472px;height:266px;background:#000;border-bottom:4px solid #2a2a2a}
.video-bar{left:20px;right:20px;bottom:40px;color:#fff;font-size:13px;display:flex;justify-content:space-between}

.stats{top:1663px;left:12px;width:1176px;height:193px;background:linear-gradient(120deg,#2b6fb3,#7fb3d9 40%,#c9dceb 60%,#2d74b4)}
.stat{top:30px;width:282px;height:150px;border:1px solid rgba(255,255,255,.6);text-align:center;color:#fff}
.stat-num{font-size:34px;margin-top:4px}
.stat-label{font-size:15px}
.stat svg{margin-top:12px}

.centered{left:0;width:1200px;text-align:center}
.center-h{font-size:42px;font-weight:400}
.center-h span{color:var(--accent)}
.center-p{font-size:14.5px;line-height:1.7;color:var(--muted);width:720px;margin:10px auto 0}

.prod{top:2035px;width:270px}
.prod-img{height:221px;background:linear-gradient(135deg,#f5f5f5,#d9dbdd)}
.prod-img.warm{background:linear-gradient(135deg,#f0f0f0,#f3a45e 60%,#d8d8d8)}
.prod h3{font-size:26px;font-weight:600;margin-top:10px}
.prod p{font-size:14.5px;line-height:1.75;color:var(--muted);margin-top:8px}
.read-more{display:block;color:var(--teal);font-size:14.5px;margin-top:14px}

.price{width:262px;border:1px solid var(--line);box-shadow:0 0 6px rgba(0,0,0,.08);text-align:center;padding:26px 16px}
.price h3{font-size:42px;font-weight:400}
.price-box{background:var(--lime);height:150px;margin-top:22px;display:flex;align-items:center;justify-content:center;font-size:30px}
.price-box sup{font-size:20px}
.price li{list-style:none;font-size:15px;color:#333;height:77px;line-height:77px;border-bottom:1px solid var(--line)}
.price li:last-child{border-bottom:none}
.btn-teal{display:inline-block;background:var(--teal);color:#fff;font-size:15px;padding:6px 14px;border-radius:3px}

.recent{top:3540px;left:12px;width:1176px;height:880px;background:var(--band)}
.filters{top:3704px;left:0;width:1200px;display:flex;justify-content:center;gap:10px}
.filters span{border:1px solid #ccc;background:#fff;font-size:14px;padding:3px 9px}
.filters span.on{background:var(--accent);color:var(--accent);border-color:var(--accent)}
.tile{width:366px;background:linear-gradient(135deg,#fbfbfb,#d8dadc)}

.contact-item{left:28px;display:flex;gap:18px;font-size:15px;line-height:1.55;color:#333}
.icon-box{width:56px;height:56px;display:flex;align-items:center;justify-content:center;margin-top:10px}
.field{left:616px;width:574px;height:40px;border:1px solid #ccc;font-size:15px;color:#888;padding:8px 12px}
.map{top:4864px;left:12px;width:1176px;height:394px;background:linear-gradient(135deg,#eae6df,#f3efe8 40%,#dfe8d7 70%,#ecd9a8)}
.footer{top:5258px;left:0;width:1200px;height:82px;background:var(--footer);color:#fff;font-size:16px;text-align:center;line-height:82px}
</style>
</head>
<body>

<header class="site-header abs">
  <div class="brand abs"><span class="brand-dot"></span>Torven Medical</div>
  <nav class="main-nav abs"><a>Home</a><a>About Us</a><a>Services</a><a>Products</a><a>Insights</a><a>Contact us</a></nav>
</header>

<section class="hero abs" role="img" aria-label="Gloved hand arranging surgical instruments on a teal drape">
  <div class="hero-arrow abs" style="left:80px">&#8249;</div>
  <div class="hero-arrow abs" style="right:80px">&#8250;</div>
  <div class="hero-copy abs">
    <div class="hero-kicker">We are specialized in orthopedic instruments</div>
    <div class="hero-title">BEST <span>quality</span> Instruments</div>
    <p class="hero-text">Lorem ipsum dolor sit amet, consectetur adipisicing elit. Reprehenderit dolore culpa incidunt veniam eaque, quod beatae animi eligendi omnis recusandae.</p>
    <a class="btn-brown">Read more</a>
  </div>
  <div class="hero-dots abs"><i></i><i></i><i></i></div>
</section>

<div class="about-img abs" role="img" aria-label="Tray of sterile surgical instruments"></div>
<section class="about-copy abs">
  <div class="eyebrow">About us</div>
  <h2 class="section-h" style="margin-top:10px">high-quality products at a significantly <span>lower cost</span></h2>
  <p class="body-text" style="margin-top:14px">Hospitals are increasingly seeking ways to cut cost while continuing to deliver high quality medical care. Torven Medical was created to offer hospitals and physicians high-quality products at a significantly lower cost. Torven Medical focus is on the orthopedic disposable market by providing quality generic products that are utilized to replace many legacy products that have low physician preference and are subject to 5%-10% annual unsustainable price increases. Torven Medical works directly with hospital administrators, department heads, and physicians to reduce cost that is incurred by a traditional medical device sales force.</p>
</section>

<section class="activity-copy abs">
  <div class="eyebrow">Our Activity</div>
  <h2 class="section-h" style="margin-top:10px">Watch our latest <span>medical Activities</span> video</h2>
  <p class="body-text" style="margin-top:14px">Lorem ipsum dolor sit amet, consectetur adipisicing elit. Nesciunt consequuntur sequi cum odit quis veniam eaque! Fugit dolorum, pariatur atque necessitatibus architecto, voluptatibus expedita saepe suscipit officiis quibusdam quas eius tempora asperiores provident perspiciatis, temporibus voluptatem. Tempora odio blanditiis dolores, excepturi, quod magni assumenda laudantium consequuntur eligendi, eos laboriosam eum doloremque explicabo sit dolor mollitia rem. Obcaecati quas error, reiciendis dolorum earum aperiam vero autem ut laboriosam iste dolores labore deserunt, quos at. Veritatis omnis consectetur quaerat obcaecati quibusdam atque!</p>
</section>
<div class="video abs">
  <div class="video-bar abs"><span>&#9654;&nbsp;&nbsp; 0:00 / 4:38</span><span>&#128264;&nbsp;&nbsp;&#9974;&nbsp;&nbsp;&#8942;</span></div>
</div>

<section class="stats abs" role="img" aria-label="Surgeons at work in a blue-lit operating room">
  <div class="stat abs" style="left:12px"><svg width="30" height="30" viewBox="0 0 30 30"><circle cx="15" cy="15" r="13" fill="none" stroke="#fff" stroke-width="3"/><circle cx="15" cy="15" r="5" fill="#fff"/></svg><div class="stat-num">1420</div><div class="stat-label">Total products</div></div>
  <div class="stat abs" style="left:302px"><svg width="30" height="30" viewBox="0 0 30 30"><circle cx="15" cy="15" r="13" fill="none" stroke="#fff" stroke-width="3"/><circle cx="15" cy="15" r="5" fill="#fff"/></svg><div class="stat-num">50</div><div class="stat-label">Total Members</div></div>
  <div class="stat abs" style="left:592px"><svg width="30" height="30" viewBox="0 0 30 30"><circle cx="15" cy="15" r="13" fill="none" stroke="#fff" stroke-width="3"/><circle cx="15" cy="15" r="5" fill="#fff"/></svg><div class="stat-num">80</div><div class="stat-label">Total companies</div></div>
  <div class="stat abs" style="left:882px"><svg width="30" height="30" viewBox="0 0 30 30"><circle cx="15" cy="15" r="13" fill="none" stroke="#fff" stroke-width="3"/><circle cx="15" cy="15" r="5" fill="#fff"/></svg><div class="stat-num">300</div><div class="stat-label">Our total selling</div></div>
</section>

<section class="centered abs" style="top:1880px">
  <h2 class="center-h">Our special products</h2>
  <p class="center-p">Lorem ipsum dolor sit amet, consectetur adipisicing elit. Quibusdam laboriosam eum, minus, aliquam, suscipit totam aspernatur labore vero maxime quas quam aperiam ea ullam. Eaque voluptate porro numquam illo laborum.</p>
</section>
<article class="prod abs" style="left:12px"><div class="prod-img warm" role="img" aria-label="Bone drill bits"></div><h3>Bone drills</h3><p>Lorem ipsum dolor sit amet, consectetur adipisicing elit. Hic, dolorem rerum exercitationem, autem nemo cupiditate, dignissimos dolores aperiam rem perferendis cumque sit, voluptates asperiores excepturi laborum officia ut nobis repellat.</p><a class="read-more">Read More</a></article>
<article class="prod abs" style="left:314px"><div class="prod-img" role="img" aria-label="Surgical bone saw blade"></div><h3>Bone saws</h3><p>Lorem ipsum dolor sit amet, consectetur adipisicing elit. Hic, dolorem rerum exercitationem, autem nemo cupiditate, dignissimos dolores aperiam rem perferendis cumque sit, voluptates asperiores excepturi laborum officia ut nobis repellat.</p><a class="read-more">Read More</a></article>
<article class="prod abs" style="left:616px"><div class="prod-img" role="img" aria-label="Set of k-wires"></div><h3>k-wires</h3><p>Lorem ipsum dolor sit amet, consectetur adipisicing elit. Hic, dolorem rerum exercitationem, autem nemo cupiditate, dignissimos dolores aperiam rem perferendis cumque sit, voluptates asperiores excepturi laborum officia ut nobis repellat.</p><a class="read-more">Read More</a></article>
<article class="prod abs" style="left:918px"><div class="prod-img" role="img" aria-label="Silver medical pin"></div><h3>pins</h3><p>Lorem ipsum dolor sit amet, consectetur adipisicing elit. Hic, dolorem rerum exercitationem, autem nemo cupiditate, dignissimos dolores aperiam rem perferendis cumque sit, voluptates asperiores excepturi laborum officia ut nobis repellat.</p><a class="read-more">Read More</a></article>

<section class="centered abs" style="top:2600px">
  <h2 class="center-h">Our <span>pricing</span> plan</h2>
  <p class="center-p">Lorem ipsum dolor sit amet, consectetur adipisicing elit. Maiores, ab, quibusdam. Vero praesentium est temporibus, molestias rerum, repellat suscipit inventore!</p>
</section>
<div class="price abs" style="left:30px;top:2736px"><h3>bone drills</h3><div class="price-box">50%<sup>off</sup></div><ul><li>lorem ispam</li><li>lorem ispam</li><li>lorem ispam</li><li>lorem ispam</li><li>lorem ispam</li><li>lorem ispam</li></ul><a class="btn-teal">Order now</a></div>
<div class="price abs" style="left:320px;top:2744px"><h3>bone saws</h3><div class="price-box">60%<sup>off</sup></div><ul><li>lorem ispam</li><li>lorem ispam</li><li>lorem ispam</li><li>lorem ispam</li><li>lorem ispam</li><li>lorem ispam</li></ul><a class="btn-teal">Order now</a></div>
<div class="price abs" style="left:610px;top:2744px"><h3>k-wires</h3><div class="price-box">50%<sup>off</sup></div><ul><li>lorem ispam</li><li>lorem ispam</li><li>lorem ispam</li><li>lorem ispam</li><li>lorem ispam</li><li>lorem ispam</li></ul><a class="btn-teal">Order now</a></div>
<div class="price abs" style="left:900px;top:2744px"><h3>pins</h3><div class="price-box">20%<sup>off</sup></div><ul><li>lorem ispam</li><li>lorem ispam</li><li>lorem ispam</li><li>lorem ispam</li><li>lorem ispam</li><li>lorem ispam</li></ul><a class="btn-teal">Order now</a></div>

<section class="recent abs"></section>
<section class="centered abs" style="top:3592px">
  <h2 class="center-h">Our recent<span>Products</span></h2>
  <p class="center-p" style="margin-top:6px">we have superior quality products and cost saving products you want.</p>
</section>
<div class="filters abs"><span class="on">All</span><span>bone drills</span><span>bone saws</span><span>k-wires</span><span>Pins</span></div>
<div class="tile abs" style="left:20px;top:3740px;height:308px;background:linear-gradient(135deg,#eee,#f3a45e 60%,#ddd)" role="img" aria-label="Bone drill bits"></div>
<div class="tile abs" style="left:404px;top:3740px;height:308px" role="img" aria-label="Surgical bone saw blade"></div>
<div class="tile abs" style="left:790px;top:3740px;height:248px" role="img" aria-label="Set of k-wires"></div>
<div class="tile abs" style="left:20px;top:4062px;height:236px" role="img" aria-label="Surgical retractor"></div>
<div class="tile abs" style="left:404px;top:4062px;height:296px" role="img" aria-label="Silver medical pin"></div>
<div class="tile abs" style="left:790px;top:4062px;height:258px" role="img" aria-label="Cordless surgical bone drill"></div>

<section class="centered abs" style="top:4440px">
  <h2 class="center-h" style="font-size:34px;font-weight:600;color:var(--accent)">Contact Us</h2>
  <p class="center-p" style="margin-top:6px">Lorem ipsum dolor sit amet, consectetur adipisicing elit. Voluptatem asperiores nihil, tempora saepe vel veritatis dignissimos laudantium distinctio error architecto.</p>
</section>
<div class="contact-item abs" style="top:4550px"><div class="icon-box"><svg width="46" height="36" viewBox="0 0 46 36"><rect x="1" y="1" width="44" height="34" fill="#222"/><path d="M4 5 L23 20 L42 5" stroke="#fff" stroke-width="3" fill="none"/></svg></div><div>Our location<br>14/c Harlow house<br>Brenton bridge road</div></div>
<div class="contact-item abs" style="top:4638px"><div class="icon-box"><svg width="50" height="36" viewBox="0 0 50 36"><circle cx="10" cy="26" r="8" fill="none" stroke="#222" stroke-width="3"/><circle cx="40" cy="26" r="8" fill="none" stroke="#222" stroke-width="3"/><path d="M10 26 L22 14 L32 14 L40 26 M18 14 L28 6" stroke="#222" stroke-width="4" fill="none"/></svg></div><div>Our location<br>14/c Harlow house<br>Brenton bridge road</div></div>
<div class="contact-item abs" style="top:4726px"><div class="icon-box"><svg width="44" height="44" viewBox="0 0 44 44"><path d="M22 2 L26 18 L42 26 L26 26 L24 38 L30 42 L14 42 L20 38 L18 26 L2 26 L18 18 Z" fill="#222" transform="rotate(90 22 22)"/></svg></div><div>Our location<br>14/c Harlow house<br>Brenton bridge road</div></div>
<div class="field abs" style="top:4554px">Your Name</div>
<div class="field abs" style="top:4602px">Your Email</div>
<div class="field abs" style="top:4650px">Your Subject</div>
<div class="field abs" style="top:4700px;height:112px;padding:40px 50px">Write your name</div>
<a class="btn-brown abs" style="left:866px;top:4812px;margin:0">Submit</a>

<div class="map abs" role="img" aria-label="Street map showing the office location"></div>
<footer class="footer abs">Copyright@2017,All rights reserved to Torven Medical</footer>

</body>
</html>
```